Project Report for American Indian and Alaska Native org (U.S.)

We need a report formatted/ design / layout.
We are a nonprofit organization that works on indigenous elder issues.
The report should reflect our logo color scheme.
Body font should be at least 11 point sans serif.
Ideally, headings and title would use fonts that are reminiscent of tribal cultures though not hard to read or whimsical/ unprofessional looking.

We have used some light script style fonts in the past -- nothing too cursive looking though.

The audience is public health professionals and tribal staff and leadership.

We want our organization's logo (QR7) and the project logo (brain health) incorporated into the title page.

We prefer the files to come back to us in an editable fashion + a pdf file.

Industry/Entity Type

tribal communities and public health officials

Font styles to use
Serif
Sans Serif

Requirements
Must have
• our logo and color scheme
Should not have
• headdress images

```html
<!DOCTYPE html>
<html lang="en">
<head>
<meta charset="utf-8">
<title>Tribal Law and Policy: Alzheimer's Disease and Related Dementia Issues</title>
<link rel="stylesheet" href="https://fonts.googleapis.com/css2?family=Arimo:wght@400;700&family=Big+Shoulders+Stencil+Display:wght@800&display=swap">
<style>
  :root {
    --clay: #b55c50;
    --teal: #52a9b2;
    --ink: #111111;
    --paper: #ffffff;
  }
  html, body {
    margin: 0;
    padding: 0;
    overflow: hidden;
    background: var(--paper);
  }
  .title-page {
    position: relative;
    width: 1200px;
    height: 848px;
    background: var(--paper);
    overflow: hidden;
    font-family: "Arimo", Arial, sans-serif;
  }
  .brand {
    position: absolute;
    display: flex;
    align-items: center;
    gap: 12px;
    font-family: "Arimo", Arial, sans-serif;
    font-weight: 700;
    color: var(--teal);
    line-height: 1.15;
    text-transform: uppercase;
  }
  .brand-mark {
    flex: none;
    background: var(--teal);
  }
  .brand--project {
    left: 185px;
    top: 51px;
    font-size: 17px;
  }
  .brand--project .brand-mark {
    width: 66px;
    height: 66px;
    border-radius: 50%;
  }
  .brand--org {
    left: 716px;
    top: 58px;
    font-size: 17px;
  }
  .brand--org .brand-mark,
  .brand--client .brand-mark {
    width: 44px;
    height: 44px;
  }
  .brand--client {
    left: 446px;
    top: 699px;
    font-size: 17px;
  }
  .report-title {
    position: absolute;
    left: 0;
    top: 0;
    margin: 0;
    width: 1200px;
    height: 600px;
  }
  .report-title text {
    font-family: "Big Shoulders Stencil Display", "Arial Narrow", sans-serif;
    font-weight: 800;
    font-size: 88px;
  }
  .report-title .line-clay { fill: var(--clay); }
  .report-title .line-teal { fill: var(--teal); }
  .credits {
    position: absolute;
    left: 0;
    top: 603px;
    width: 1200px;
    margin: 0;
    text-align: center;
    font-size: 19px;
    line-height: 23.5px;
    color: var(--ink);
  }
</style>
</head>
<body>
<main class="title-page">
  <div class="brand brand--project">
    <span class="brand-mark"></span>
    <span>Native Elders<br>Brain Wellness Hub</span>
  </div>
  <div class="brand brand--org">
    <span class="brand-mark"></span>
    <span>QR7 · Global Council<br>for Native Elders</span>
  </div>

  <h1 class="report-title" aria-label="Tribal Law and Policy: Alzheimer's Disease and Related Dementia Issues">
    <svg width="1200" height="600" viewBox="0 0 1200 600" aria-hidden="true">
      <text class="line-clay" x="199" y="244" textLength="776" lengthAdjust="spacingAndGlyphs">TRIBAL LAW AND POLICY:</text>
      <text class="line-teal" x="253" y="346" textLength="667" lengthAdjust="spacingAndGlyphs">ALZHEIMER'S DISEASE</text>
      <text class="line-teal" x="529" y="449" textLength="114" lengthAdjust="spacingAndGlyphs">AND</text>
      <text class="line-teal" x="170" y="551" textLength="834" lengthAdjust="spacingAndGlyphs">RELATED DEMENTIA ISSUES</text>
    </svg>
  </h1>

  <p class="credits">Prepared by Larkfield Consulting<br>October 27, 2021<br>For</p>

  <div class="brand brand--client">
    <span class="brand-mark"></span>
    <span>QR7 · Global Council<br>for Native Elders</span>
  </div>
</main>
</body>
</html>
```